Bright, Fun and hard to forget home inspection business card.

We need a Business card design for a new Home Inspection company. We are building a brand that is bright, fun and easy to remember.

Target Market(s)

Anyone involed in buying and selling of homes.

Industry/Entity Type

Home Inspection

Contact Information for Business Card

Colin Marlowe Owner/Inspector

Wedsite- PorchAndRafterCheck.example
Phone: 253-555-0187
Email- ColinMarlowe@mailbox.example
WA Lic # 4806

Requirements
Must have
• BRQV LOGO somewhere on card.

```html
<!DOCTYPE html>
<html lang="en">
<head>
<meta charset="utf-8">
<title>Porch and Rafter Check – Business Card</title>
<link rel="stylesheet" href="https://fonts.googleapis.com/css2?family=Open+Sans:wght@400;600;700&display=swap">
<style>
  :root {
    --backdrop: #8a6040;
    --card-white: #f7f6f3;
    --brand-orange: #f05a28;
    --ink: #1b1b1b;
    --swoosh-grey: #d9d9d9;
    --text-light: #ffffff;
  }
  * { box-sizing: border-box; margin: 0; padding: 0; }
  html, body { width: 1200px; height: 480px; overflow: hidden; }
  body {
    background: var(--backdrop);
    font-family: "Open Sans", Arial, sans-serif;
    position: relative;
  }
  .card {
    position: absolute;
    top: 100px;
    width: 466px;
    height: 262px;
    background: var(--card-white);
    overflow: hidden;
  }
  .card--front { left: 86px; }
  .card--back { left: 592px; }
  .card__waves { position: absolute; inset: 0; width: 100%; height: 100%; }

  .brand {
    position: absolute;
    display: flex;
    align-items: center;
    gap: 12px;
    font-weight: 700;
    line-height: 1.05;
    text-transform: uppercase;
  }
  .brand__dot {
    flex: none;
    border-radius: 50%;
    background: var(--brand-orange);
  }
  .card--front .brand { left: 58px; top: 34px; color: var(--ink); font-size: 30px; }
  .card--front .brand__dot { width: 44px; height: 44px; }
  .card--back .brand { left: 122px; top: 72px; color: var(--brand-orange); font-size: 28px; }
  .card--back .brand__dot { width: 40px; height: 40px; }

  .person {
    position: absolute;
    left: 26px;
    top: 206px;
    color: var(--text-light);
  }
  .person__name { font-size: 16px; font-weight: 700; }
  .person__role { font-size: 11px; font-weight: 400; margin-top: 4px; }

  .contact {
    position: absolute;
    right: 22px;
    top: 160px;
    list-style: none;
    color: var(--text-light);
    text-align: right;
    font-size: 11.5px;
  }
  .contact li { display: flex; justify-content: flex-end; align-items: center; gap: 8px; height: 24px; }
  .contact__licence { padding-right: 2px; }
  .contact__site { font-weight: 700; font-size: 13px; }
  .contact svg { width: 12px; height: 12px; flex: none; }

  .back-url {
    position: absolute;
    left: 0; right: 0;
    top: 214px;
    text-align: center;
    color: var(--brand-orange);
    font-size: 12px;
    font-weight: 600;
  }
</style>
</head>
<body>

<section class="card card--front" aria-label="Business card front">
  <svg class="card__waves" viewBox="0 0 466 262" preserveAspectRatio="none" aria-hidden="true">
    <path d="M0 146 C120 150 220 170 300 150 C380 130 430 92 466 84 L466 110 C420 118 370 150 300 168 C220 188 120 170 0 160 Z" fill="var(--ink)"/>
    <path d="M0 162 C120 172 220 190 300 172 C380 152 430 118 466 112 L466 124 C420 132 370 160 300 180 C220 200 120 186 0 176 Z" fill="var(--swoosh-grey)"/>
    <path d="M0 180 C120 192 220 206 300 186 C380 166 430 134 466 126 L466 262 L0 262 Z" fill="var(--brand-orange)"/>
  </svg>

  <div class="brand">
    <span class="brand__dot"></span>
    <span>Porch and<br>Rafter Check</span>
  </div>

  <div class="person">
    <p class="person__name">Colin Marlowe</p>
    <p class="person__role">Owner / Inspecto</p>
  </div>

  <ul class="contact">
    <li class="contact__licence">WA Lic # 4806</li>
    <li>253-555-0187
      <svg viewBox="0 0 12 12"><circle cx="6" cy="6" r="5.5" fill="none" stroke="#fff"/><path d="M4 3.5 L5 5 L4.5 5.6 Q5.5 7 6.6 7.6 L7.2 7 L8.6 8 L8 9 Q5 8.6 3.4 4.4 Z" fill="#fff"/></svg>
    </li>
    <li>ColinMarlowe@mailbox.example
      <svg viewBox="0 0 12 12"><rect x="1" y="3" width="10" height="7" fill="#fff"/><path d="M1 3 L6 7 L11 3" fill="none" stroke="var(--brand-orange)"/></svg>
    </li>
    <li class="contact__site">PorchAndRafterCheck.example
      <svg viewBox="0 0 12 12"><circle cx="6" cy="6" r="5" fill="none" stroke="#fff"/><ellipse cx="6" cy="6" rx="2.2" ry="5" fill="none" stroke="#fff"/><path d="M1 6 H11" stroke="#fff"/></svg>
    </li>
  </ul>
</section>

<section class="card card--back" aria-label="Business card back">
  <div class="brand">
    <span class="brand__dot"></span>
    <span>Porch and<br>Rafter Check</span>
  </div>
  <p class="back-url">www.PorchAndRafterCheck.example</p>
</section>

</body>
</html>
```